Website for The Velvet Pathfinder

We need an impressive e-commerce website for our newly launched business "The Velvet Pathfinder".
The Velvet Pathfinder searches store-front and online retailers for diamond engagement rings according to the client's specified requirements. We want to save people time by doing the shopping around for them.
We can relate to, and we love, www.corvaline.com
Like corvaline.com, we want to offer website visitors a quick run-down on how the process works, then offer them to elect a service package and pay for that package on the spot.
Content pages:
HOME
HOW IT WORKS
DIAMOND GALLERY
ABOUT
FAQs
CONTACT
Inclusions: Our logo and Facebook and Instagram buttons
We want to be able to easily edit this website, We want it to display well on iPhone and android, We want it to be clean and striking.
Like our logo, we want our website to embody elegant masculinity.
Target Market(s)
Men in market for diamond ring purchase $5k - $50k
Industry/Entity Type
Business
Number of Pages Required
5+ page
Font styles to use
Look and feel

```html
<!DOCTYPE html>
<html lang="en">
<head>
<meta charset="utf-8">
<title>About Us — The Velvet Pathfinder</title>
<link rel="stylesheet" href="https://fonts.googleapis.com/css2?family=Bebas+Neue&family=Lato:wght@400;700&family=Oswald:wght@400;500&display=swap">
<style>
:root{
  --ink:#333;
  --body:#666;
  --nav:#555;
  --nav-active:#8c8c8c;
  --band-top:#9a9a9a;
  --band-bottom:#6e6e6e;
  --crumb:#d2d2d2;
  --story:#dcdcdc;
  --slate:#636363;
  --footer:#222;
  --base:#0d0d0d;
  --white:#fff;
}
*{box-sizing:border-box;margin:0;padding:0}
html,body{width:1200px;height:2186px;overflow:hidden;background:var(--white)}
body{font-family:"Lato",sans-serif;color:var(--body);position:relative}
.abs{position:absolute}
.topline{top:0;left:0;width:1200px;height:8px;background:#444}
.header{top:8px;left:0;width:1200px;height:182px}
.header-left{left:160px;top:80px;font-size:12px;color:#555}
.header-right{right:160px;top:80px;font-size:12px;color:#555;display:flex;gap:8px;align-items:center}
.brand{left:0;width:1200px;top:50px;text-align:center;font-family:"Lato",sans-serif;font-weight:700;color:#555}
.brand .mark{display:block;width:58px;height:58px;border:2px solid #777;border-radius:50%;margin:0 auto 12px}
.brand .name{font-size:15px;letter-spacing:2px;text-transform:uppercase;line-height:18px}
.nav{top:190px;left:0;width:1200px;height:38px;background:var(--nav);display:flex;justify-content:center}
.nav a{color:var(--white);text-decoration:none;font-size:12px;text-transform:uppercase;line-height:38px;padding:0 33px}
.nav a.active{background:var(--nav-active)}
.page-title{top:228px;left:0;width:1200px;height:192px;background:linear-gradient(var(--band-top),var(--band-bottom));text-align:center}
.page-title h1{font-family:"Bebas Neue",sans-serif;font-weight:400;color:var(--white);font-size:62px;line-height:192px;letter-spacing:1px}
.crumb{top:420px;left:0;width:1200px;height:37px;background:var(--crumb);font-size:12px;color:#444;padding-left:164px;line-height:37px}
.story{top:457px;left:0;width:1200px;height:516px;background:radial-gradient(ellipse at 45% 30%,#cfcfcf,#e2e2e2 55%,#d4d4d4)}
.story-col{top:528px;width:426px}
.story-col h2{display:flex;align-items:baseline;gap:6px;color:#444;margin-bottom:6px}
.story-col h2 .num{font-family:"Oswald",sans-serif;font-size:50px;font-weight:400;line-height:50px}
.story-col h2 .label{font-size:19px;font-weight:700;letter-spacing:1px;text-transform:uppercase}
.story-col p{font-size:12.5px;line-height:18px;margin-bottom:18px;color:#555;text-align:justify}
.portrait{top:1060px;left:164px;width:273px;height:400px;background:linear-gradient(#e8e8e8,#8d8f93 60%,#6f7176)}
.profile{top:1058px;left:463px;width:580px}
.profile h2{font-family:"Oswald",sans-serif;font-weight:400;font-size:31px;color:#444;text-transform:uppercase}
.profile .intro{font-size:12.5px;line-height:18px;margin-top:6px;color:#666}
.trait{position:absolute;left:0;display:flex;gap:16px}
.trait svg{flex:none}
.trait h3{font-family:"Oswald",sans-serif;font-weight:400;font-size:19px;color:#444;text-transform:uppercase;line-height:22px}
.trait p{font-size:12px;line-height:17px;color:#666;width:500px}
.slate{top:1552px;left:0;width:1200px;height:328px;background:var(--slate)}
.slate-col{top:1628px;width:426px;color:var(--white);font-size:12.5px;line-height:18px;text-align:justify}
.slate-col p{margin-bottom:18px}
.footer{top:1880px;left:0;width:1200px;height:262px;background:var(--footer);color:var(--white);font-size:12px;line-height:17px}
.f-about{left:164px;top:48px;width:290px}
.f-about p{margin-bottom:16px}
.f-links{left:462px;top:48px;list-style:none}
.f-links li{line-height:17px}
.f-info{left:590px;top:44px;width:290px;color:#bbb}
.f-info h4{font-family:"Oswald",sans-serif;font-weight:400;color:var(--white);font-size:16px;margin-bottom:18px}
.pay{left:892px;top:50px;width:150px;height:46px;border:2px solid #ccc;border-radius:4px;background:#f4f4f4;display:flex;gap:8px;align-items:center;justify-content:center}
.pay span{width:28px;height:18px;border-radius:2px;background:#7c8fb3}
.social{left:892px;top:120px;display:flex;gap:14px}
.social span{width:28px;height:28px;background:#777}
.base{top:2142px;left:0;width:1200px;height:44px;background:var(--base);color:#ddd;font-size:12px;text-align:center;line-height:44px}
</style>
</head>
<body>
<div class="abs topline"></div>
<header class="abs header">
  <div class="abs header-left">$ ▾ &nbsp; | &nbsp;📞 888-410-2267</div>
  <div class="abs brand"><span class="mark"></span><span class="name">The Velvet<br>Pathfinder</span></div>
  <div class="abs header-right">Wish List (0) |
    <svg width="12" height="12" viewBox="0 0 12 12"><circle cx="5" cy="5" r="3.5" fill="none" stroke="#555" stroke-width="1.5"/><line x1="7.5" y1="7.5" x2="11" y2="11" stroke="#555" stroke-width="1.5"/></svg>
    <svg width="12" height="12" viewBox="0 0 12 12"><circle cx="6" cy="4" r="2.5" fill="#555"/><path d="M1 12a5 5 0 0 1 10 0z" fill="#555"/></svg>
    <svg width="13" height="12" viewBox="0 0 13 12"><path d="M0 1h2l2 7h7l2-5H3" fill="none" stroke="#555" stroke-width="1.4"/><circle cx="5" cy="10.5" r="1.2" fill="#555"/><circle cx="10" cy="10.5" r="1.2" fill="#555"/></svg>
  </div>
</header>
<nav class="abs nav">
  <a href="#">Home</a><a href="#" class="active">About Us</a><a href="#">How It Works</a><a href="#">Diamond Gallery</a><a href="#">Faqs</a><a href="#">Contact</a>
</nav>
<section class="abs page-title"><h1>About Us</h1></section>
<div class="abs crumb">Home &gt; About Us</div>

<section class="abs story" role="img" aria-label="Faded photograph of a rocky seashore"></section>
<article class="abs story-col" style="left:164px">
  <h2><span class="num">01</span><span class="label">History</span></h2>
  <p>Nulla molestie dapibus vestibulum. Phasellus pharetra imperdiet justo ac scelerisque. Duis sagittis, arcu id accumsan iaculis, nulla arcu porta est, quis porta ipsum metus ut nibh. Donec ante erat, viverra ornare euismod ut, vulputate vel erat.</p>
  <p>Pellentesque rutrum dignissim neque rhoncus pulvinar. Fusce a dictum diam. Maecenas ac mollis nisl, et faucibus dolor. Duis semper cursus nisl, quis sodales sapien. Vestibulum dapibus tortor quis lacinia rutrum.</p>
  <p>Praesent pulvinar tempus massa ac pretium. Morbi quis enim ultricies, sollicitudin lorem dictum, lacinia dui. Vivamus placerat erat eu metus tempus pellentesque. Nulla eu magna scelerisque neque rutrum pellentesque sed ut lacus.</p>
  <p>In blandit sem augue, et tempus nibh suscipit ac. Nunc eget ipsum a ante vehicula euismod a ut quam. Interdum et malesuada fames ac ante ipsum primis in faucibus. Morbi sollicitudin viverra blandit. Aenean congue iaculis quam at lobortis.</p>
  <p>Nullam hendrerit finibus lacus eget dictum. Etiam eu ipsum a nibh gravida blandit quis nec felis. Proin feugiat odio magna, non ullamcorper.</p>
</article>
<article class="abs story-col" style="left:614px">
  <h2><span class="num">02</span><span class="label">Mission</span></h2>
  <p>Nulla molestie dapibus vestibulum. Phasellus pharetra imperdiet justo ac scelerisque. Duis sagittis, arcu id accumsan iaculis, nulla arcu porta est, quis porta ipsum metus ut nibh. Donec ante erat, viverra ornare euismod ut, vulputate vel erat.</p>
  <p>Pellentesque rutrum dignissim neque rhoncus pulvinar. Fusce a dictum diam. Maecenas ac mollis nisl, et faucibus dolor. Duis semper cursus nisl, quis sodales sapien. Vestibulum dapibus tortor quis lacinia rutrum.</p>
  <p>Praesent pulvinar tempus massa ac pretium. Morbi quis enim ultricies, sollicitudin lorem dictum, lacinia dui. Vivamus placerat erat eu metus tempus pellentesque. Nulla eu magna scelerisque neque rutrum pellentesque sed ut lacus.</p>
  <p>In blandit sem augue, et tempus nibh suscipit ac. Nunc eget ipsum a ante vehicula euismod a ut quam. Interdum et malesuada fames ac ante ipsum primis in faucibus. Morbi sollicitudin viverra blandit. Aenean congue iaculis quam at lobortis.</p>
  <p>Nullam hendrerit finibus lacus eget dictum. Etiam eu ipsum a nibh gravida blandit quis nec felis. Proin feugiat odio magna, non ullamcorper.</p>
</article>

<div class="abs portrait" role="img" aria-label="Portrait of the founder in a grey suit, arms folded"></div>
<section class="abs profile" style="height:420px">
  <h2>My Name Is Edmund</h2>
  <p class="intro">Suspendisse vel enim viverra, iaculis sapien auctor, porttitor risus. Nunc tincidunt dolor non iaculis fringilla. Fusce vulputate nisi et dolor facilisis euismod.</p>
  <div class="trait" style="top:116px">
    <svg width="50" height="50" viewBox="0 0 50 50"><rect x="10" y="10" width="30" height="30" transform="rotate(45 25 25)" fill="#555"/><path d="M22 31V20l8-2v10" fill="none" stroke="#fff" stroke-width="1.6"/><circle cx="20.5" cy="31" r="2" fill="#fff"/><circle cx="28.5" cy="28" r="2" fill="#fff"/></svg>
    <div><h3>Music Is My Favorite</h3><p>Donec lacinia a odio sed fermentum. Mauris quis nibh velit. Pellentesque dui tortor, commodo non neque ac, tempor cursus velit.</p></div>
  </div>
  <div class="trait" style="top:195px">
    <svg width="50" height="50" viewBox="0 0 50 50"><rect x="10" y="10" width="30" height="30" transform="rotate(45 25 25)" fill="#555"/><rect x="18" y="21" width="14" height="10" fill="#fff"/><rect x="22" y="18" width="6" height="4" fill="none" stroke="#fff" stroke-width="1.4"/></svg>
    <div><h3>My Job Is Graphic Design In Company</h3><p>Donec lacinia a odio sed fermentum. Mauris quis nibh velit. Pellentesque dui tortor, commodo non neque ac, tempor cursus velit.</p></div>
  </div>
  <div class="trait" style="top:269px">
    <svg width="50" height="50" viewBox="0 0 50 50"><rect x="10" y="10" width="30" height="30" transform="rotate(45 25 25)" fill="#555"/><circle cx="19" cy="28" r="4" fill="none" stroke="#fff" stroke-width="1.5"/><circle cx="31" cy="28" r="4" fill="none" stroke="#fff" stroke-width="1.5"/><path d="M19 28l5-6h5l2 6M24 22l-1-2" fill="none" stroke="#fff" stroke-width="1.4"/></svg>
    <div><h3>My Hobbie Is Bicycle</h3><p>Donec lacinia a odio sed fermentum. Mauris quis nibh velit. Pellentesque dui tortor, commodo non neque ac, tempor cursus velit.</p></div>
  </div>
  <div class="trait" style="top:350px">
    <svg width="50" height="50" viewBox="0 0 50 50"><rect x="10" y="10" width="30" height="30" transform="rotate(45 25 25)" fill="#555"/><path d="M19 31l10-10 2 2-10 10h-2z" fill="#fff"/></svg>
    <div><h3>I Like Drawing</h3><p>Donec lacinia a odio sed fermentum. Mauris quis nibh velit. Pellentesque dui tortor, commodo non neque ac, tempor cursus velit.</p></div>
  </div>
</section>

<section class="abs slate"></section>
<div class="abs slate-col" style="left:164px">
  <p>Nullam hendrerit finibus lacus eget dictum. Etiam eu ipsum a nibh gravida blandit quis nec felis. Proin feugiat odio magna, non ullamcorper mauris molestie sed. Mauris sit amet turpis quis augue fringilla luctus quis nec ante. Lorem ipsum dolor sit amet, consectetur adipiscing elit.</p>
  <p>Pellentesque semper interdum turpis eu aliquet. Nullam nisi mauris, varius ac augue et, semper consequat nisi. Nulla feugiat, erat vitae ultrices sagittis, odio metus auctor neque, eget pulvinar arcu purus quis sem. Vestibulum euismod semper orci, a iaculis purus molestie at.</p>
</div>
<div class="abs slate-col" style="left:614px">
  <p>Nullam hendrerit finibus lacus eget dictum. Etiam eu ipsum a nibh gravida blandit quis nec felis. Proin feugiat odio magna, non ullamcorper mauris molestie sed. Mauris sit amet turpis quis augue fringilla luctus quis nec ante. Lorem ipsum dolor sit amet, consectetur adipiscing elit.</p>
  <p>Pellentesque semper interdum turpis eu aliquet. Nullam nisi mauris, varius ac augue et, semper consequat nisi. Nulla feugiat, erat vitae ultrices sagittis, odio metus auctor neque, eget pulvinar arcu purus quis sem. Vestibulum euismod semper orci, a iaculis purus molestie at.</p>
</div>

<footer class="abs footer">
  <div class="abs f-about">
    <p>Lorem ipsum dolor sit amet, consectetur adipiscing elit. Integer gravida nisl sed sapien placerat imperdiet. Aenean id est vel orci tempor dignissim. Ut ac est velit. Aliquam lorem nulla.</p>
    <p>Aliquam placerat ultrices libero, vel hendrerit orci bibendum vitae. Donec sit amet ex sollicitudin tellus tincidunt convallis at vel nunc.</p>
  </div>
  <ul class="abs f-links">
    <li>Home</li><li>About Us</li><li>How It Works</li><li>Diamond Gallery</li><li>Faqs</li><li>Contact</li><li>Delivery Information</li><li>Privacy Policy</li><li>Terms &amp; Conditions</li>
  </ul>
  <div class="abs f-info">
    <h4>INFO CONTACT</h4>
    <p>Address: VelvetPathfinder, 18 Larkspur Lane 40512 Lyon France</p>
    <p style="margin-top:4px">Telephone: 0145-882-310</p>
    <p>Email: hello@velvetpathfinder.com</p>
  </div>
  <div class="abs pay"><span></span><span style="background:#b9b9b9"></span><span style="background:#9aa6b8"></span></div>
  <div class="abs social"><span></span><span></span><span></span><span></span></div>
</footer>
<div class="abs base">Copyright 2016 VelvetPathfinder. All Rights Reserved.</div>
</body>
</html>
```